Brackenmoor - Healthcare Brochure - B2B

We need a new brochure design, we're satisfied with the copy but were just looking for complete overhaul of the design. Please see an example of the old design attached. It was just a template we filled out.
Requirements
Nice to have
- The second attachment is an example of a style we like

```html
<!DOCTYPE html>
<html lang="en">
<head>
<meta charset="utf-8">
<title>Brackenmoor – Post-acute Care Brochure</title>
<link href="https://fonts.googleapis.com/css2?family=Poppins:ital,wght@0,400;0,500;0,600;0,700;1,400&display=swap" rel="stylesheet">
<style>
  :root{
    --blue:#1a78be;
    --ink:#1c1c1c;
    --text:#3a3a3a;
    --panel-grey:#f3f3f5;
    --paper:#ffffff;
    --backdrop:#e8e8e8;
    --photo-a:#8fb3d6;
    --photo-b:#e6ecf3;
  }
  *{margin:0;padding:0;box-sizing:border-box}
  html,body{width:797px;height:1200px;overflow:hidden;background:var(--backdrop);font-family:'Poppins',sans-serif;color:var(--text)}
  .canvas{position:relative;width:797px;height:1200px}
  .sheet{position:absolute;width:576px;height:445px;background:var(--paper);overflow:hidden}
  .sheet--outside{left:106px;top:92px}
  .sheet--inside{left:117px;top:611px}
  .abs{position:absolute}

  /* outside sheet */
  .about-panel{left:0;top:0;width:192px;height:445px;background:var(--panel-grey)}
  .contact-panel{left:192px;top:0;width:192px;height:445px;background:var(--blue);color:#fff;text-align:center}
  .cover-panel{left:384px;top:0;width:192px;height:445px;background:var(--paper)}

  .section-title{font-size:11px;font-weight:500;color:var(--ink);line-height:1}
  .section-rule{width:30px;height:1.5px;background:var(--blue);margin-top:5px}
  .body-copy{font-size:7.5px;line-height:10.2px;color:var(--text)}

  .about-title{left:20px;top:66px}
  .about-copy{left:20px;top:86px;width:136px}
  .about-copy p+p{margin-top:10.2px}
  .quote-mark{left:21px;top:286px}
  .about-quote{left:40px;top:307px;width:124px;font-size:9.4px;line-height:10.9px;font-style:italic;color:var(--blue)}

  .contact-name{left:0;width:192px;top:128px;font-size:13px;font-weight:500;letter-spacing:.5px}
  .contact-title{left:0;width:192px;top:178px;font-size:8.8px;font-weight:500}
  .contact-rule{left:81px;top:191px;width:30px;height:1px;background:#fff}
  .contact-intro{left:46px;width:100px;top:196px;font-size:6.6px;line-height:8.8px}
  .contact-icon{left:90px;width:12px;height:12px}
  .contact-line{left:0;width:192px;font-size:6.8px;line-height:8.8px}

  .brand-mark{left:20px;top:31px;width:24px;height:22px;background:var(--blue)}
  .brand-name{left:50px;top:31px;font-size:17px;font-weight:700;color:var(--ink);line-height:22px;letter-spacing:.2px}
  .cover-photo{left:0;top:67px;width:192px;height:250px;background:linear-gradient(160deg,var(--photo-a),var(--photo-b) 70%,#cfd8e4)}
  .tagline-band{left:0;top:317px;width:192px;height:14px;background:var(--blue);color:#fff;font-size:7px;line-height:14px;padding-left:20px}
  .cover-headline{left:20px;top:339px;font-size:16px;font-weight:700;line-height:17px;color:var(--ink)}
  .cover-sub{left:20px;top:376px;font-size:12px;color:var(--blue);line-height:14px}
  .cover-note{left:20px;top:396px;width:150px;font-size:7px;line-height:9.6px;font-style:italic;color:var(--ink)}

  /* inside sheet */
  .mission-panel{left:0;top:19px;width:192px;height:212px;background:var(--panel-grey)}
  .mission-title{left:20px;top:65px}
  .mission-copy{left:20px;top:85px;width:140px}
  .mission-photo{left:192px;top:0;width:344px;height:231px;background:linear-gradient(120deg,#e9e6e2,#d9d6d2 45%,#7fc9cf 75%,#4bb5bd)}
  .side-strip{left:536px;top:22px;width:40px;height:209px;background:var(--panel-grey)}
  .accent-block{left:485px;top:22px;width:91px;height:32px;background:var(--blue)}
  .process-dot{left:14px;top:226px;width:34px;height:34px;border-radius:50%;background:var(--blue)}
  .process-copy{left:59px;top:237px;width:440px;font-size:7.6px;line-height:10.6px;color:var(--text)}

  .feature{position:absolute;width:180px;height:48px}
  .feature-icon{position:absolute;left:0;top:2px;width:20px;height:20px}
  .feature-rule{position:absolute;left:29px;top:0;width:1px;height:48px;background:var(--blue)}
  .feature-text{position:absolute;left:34px;top:2px;width:106px}
  .feature-title{font-size:6.9px;font-weight:600;color:var(--ink);line-height:9px}
  .feature-body{font-size:6.5px;line-height:8.7px;color:var(--text);margin-top:1px}

  .footer-band{left:0;top:436px;width:576px;height:9px;background:var(--blue)}
</style>
</head>
<body>
<div class="canvas">

  <section class="sheet sheet--outside">
    <div class="abs about-panel">
      <div class="abs about-title"><h2 class="section-title">About Brackenmoor</h2><div class="section-rule"></div></div>
      <div class="abs about-copy body-copy">
        <p>At Brackenmoor, we do more than bridge the gap—we make the transition from hospital to home smooth and stress-free. From discharge to a patient’s appointment with their primary care physician, we coordinate every step, ensuring they receive the right care at the right time.</p>
        <p>For Medicare beneficiaries, this support is life-changing. Our personalized approach reduces readmissions, promotes faster recovery, and empowers patients with seamless, well-managed care from facility to home.</p>
      </div>
      <svg class="abs quote-mark" width="24" height="20" viewBox="0 0 24 20" aria-hidden="true">
        <g fill="#1a78be"><circle cx="6" cy="14" r="5.5"/><path d="M1 14 C1 6 5 2 10 1 L10 3 C6 4 4 8 4 12 Z"/><circle cx="18" cy="14" r="5.5"/><path d="M13 14 C13 6 17 2 22 1 L22 3 C18 4 16 8 16 12 Z"/></g>
      </svg>
      <p class="abs about-quote">Our process is simple, fast, and most importantly: effective. One call, and we take it from there. From your healthcare facility to their home, we’re there every step of the way.</p>
    </div>

    <div class="abs contact-panel">
      <div class="abs contact-name">BRACKENMOOR</div>
      <h3 class="abs contact-title">Get In Touch</h3>
      <div class="abs contact-rule"></div>
      <p class="abs contact-intro">Join us in transforming post-acute care. Let’s make every patient’s transition a story of success.</p>

      <svg class="abs contact-icon" style="top:236px" viewBox="0 0 12 12" aria-hidden="true"><circle cx="6" cy="6" r="6" fill="#fff"/><path d="M4.2 3.3l1 1.2-.6.7c.4.8 1 1.4 1.8 1.8l.7-.6 1.2 1-.6.9c-2 .1-4.4-2.3-4.3-4.3z" fill="#1a78be"/></svg>
      <p class="abs contact-line" style="top:253px">617-555-0142</p>

      <svg class="abs contact-icon" style="top:267px" viewBox="0 0 12 12" aria-hidden="true"><circle cx="6" cy="6" r="6" fill="#fff"/><rect x="3.6" y="5" width="4.8" height="3.2" rx=".5" fill="#1a78be"/><rect x="4.4" y="3.4" width="3.2" height="1.4" fill="#1a78be"/></svg>
      <p class="abs contact-line" style="top:284px">617-555-0187</p>

      <svg class="abs contact-icon" style="top:298px" viewBox="0 0 12 12" aria-hidden="true"><circle cx="6" cy="6" r="6" fill="#fff"/><path d="M6 2.8a2.2 2.2 0 0 0-2.2 2.2C3.8 6.7 6 9.2 6 9.2s2.2-2.5 2.2-4.2A2.2 2.2 0 0 0 6 2.8z" fill="#1a78be"/><circle cx="6" cy="5" r=".8" fill="#fff"/></svg>
      <p class="abs contact-line" style="top:315px">48 Harrow Ln, Ste 210,<br>Fenwick, MA, 02190</p>
    </div>

    <div class="abs cover-panel">
      <div class="abs brand-mark"></div>
      <div class="abs brand-name">BRACKENMOOR</div>
      <div class="abs cover-photo" role="img" aria-label="Photo: nurse in blue scrubs pushing an older patient in a wheelchair down a hospital corridor"></div>
      <div class="abs tagline-band">Bridging Gaps &amp; Improving Lives</div>
      <h1 class="abs cover-headline">Revolutionizing<br>Post-acute Care</h1>
      <p class="abs cover-sub">One patient at a time</p>
      <p class="abs cover-note">Because every patient deserves a seamless recovery.</p>
    </div>
  </section>

  <section class="sheet sheet--inside">
    <div class="abs mission-panel"></div>
    <div class="abs mission-title"><h2 class="section-title">Our Mission</h2><div class="section-rule"></div></div>
    <p class="abs mission-copy body-copy">To make the healthcare experience for every patient as fluid, efficient, and compassionate as possible. Through cutting-edge care and seamless coordination, we ensure patients recover faster, stay healthier, and never lose sight of their well-being.</p>
    <div class="abs mission-photo" role="img" aria-label="Photo: nurse in teal scrubs holding the hand of a smiling older man resting in a hospital bed"></div>
    <div class="abs side-strip"></div>
    <div class="abs accent-block"></div>

    <div class="abs process-dot"></div>
    <p class="abs process-copy">Our process is quick, straightforward, and, most importantly, effective. With just one call, we handle the rest—guiding patients seamlessly from your healthcare facility to their home, ensuring support every step of the way.</p>

    <div class="feature" style="left:21px;top:278px">
      <svg class="feature-icon" viewBox="0 0 20 20" fill="none" stroke="#444" stroke-width="1"><rect x="2" y="6" width="13" height="9" rx="1"/><path d="M15 9h2.5l1.5 3v3h-4"/><circle cx="6" cy="16" r="1.5"/><circle cx="15" cy="16" r="1.5"/><path d="M8.5 8.5v4M6.5 10.5h4"/></svg>
      <div class="feature-rule"></div>
      <div class="feature-text"><h4 class="feature-title">Seamless Transition</h4><p class="feature-body">We ensure smooth facility-to-home transitions with no gaps in care, prioritizing patient outcomes.</p></div>
    </div>
    <div class="feature" style="left:213px;top:278px">
      <svg class="feature-icon" viewBox="0 0 20 20" fill="none" stroke="#444" stroke-width="1"><path d="M2 17V4M2 13h16v4M2 10h6v3M9 10h9v3"/><circle cx="5" cy="8" r="1.4"/><path d="M4 2h3v3"/></svg>
      <div class="feature-rule"></div>
      <div class="feature-text"><h4 class="feature-title">Reduced Readmission Risk</h4><p class="feature-body">We minimize readmission risk with proactive care, enhancing outcomes and supporting value-based care goals.</p></div>
    </div>
    <div class="feature" style="left:405px;top:278px">
      <svg class="feature-icon" viewBox="0 0 20 20" fill="none" stroke="#444" stroke-width="1"><circle cx="4" cy="3.5" r="1.5"/><circle cx="16" cy="3.5" r="1.5"/><circle cx="4" cy="14.5" r="1.5"/><circle cx="16" cy="14.5" r="1.5"/><path d="M1.5 8h5M13.5 8h5M1.5 19h5M13.5 19h5"/><rect x="7.5" y="8" width="5" height="5"/><path d="M10 9.2v2.6M8.7 10.5h2.6"/></svg>
      <div class="feature-rule"></div>
      <div class="feature-text"><h4 class="feature-title">Streamlined Referral Process</h4><p class="feature-body">Easily refer patients with a fast, simple process that ensures seamless transitions in care.</p></div>
    </div>

    <div class="feature" style="left:21px;top:352px">
      <svg class="feature-icon" viewBox="0 0 20 20" fill="none" stroke="#444" stroke-width="1"><rect x="2" y="2" width="11" height="16" rx="1"/><path d="M4.5 5h6M4.5 8h6M4.5 11h4"/><rect x="13" y="11" width="5" height="7" rx="1"/><path d="M13 13.5h5"/></svg>
      <div class="feature-rule"></div>
      <div class="feature-text"><h4 class="feature-title">Prescription Refills</h4><p class="feature-body">We handle refills for non-controlled prescriptions, ensuring your patients have what they need to recover.</p></div>
    </div>
    <div class="feature" style="left:213px;top:352px">
      <svg class="feature-icon" viewBox="0 0 20 20" fill="none" stroke="#444" stroke-width="1"><rect x="3.5" y="2.5" width="13" height="16" rx="1"/><rect x="7.5" y="1" width="5" height="3"/><path d="M6 7h8M6 10h8M6 13h8M6 16h5"/></svg>
      <div class="feature-rule"></div>
      <div class="feature-text"><h4 class="feature-title">VNA Order Sign-Off</h4><p class="feature-body">We sign off on VNA orders, streamlining the process and ensuring seamless home care coordination.</p></div>
    </div>
    <div class="feature" style="left:405px;top:352px">
      <svg class="feature-icon" viewBox="0 0 20 20" fill="none" stroke="#444" stroke-width="1"><rect x="2" y="2" width="16" height="9"/><path d="M5 8l3-3 3 2 4-3"/><circle cx="5" cy="14" r="1.5"/><circle cx="10" cy="14" r="1.5"/><path d="M2.5 18.5c0-2 5-2 5 0M7.5 18.5c0-2 5-2 5 0M14 14h4M14 16.5h4"/></svg>
      <div class="feature-rule"></div>
      <div class="feature-text"><h4 class="feature-title">Patient Education</h4><p class="feature-body">Empowering patient’s with information to make informed decisions about their health.</p></div>
    </div>

    <div class="abs footer-band"></div>
  </section>

</div>
</body>
</html>
```